brovalux business card

We are a commercial cleaning/janitorial service company our main target is building owners and managers.
Would like to see the icon as a background shadow in the front and the full logo in white on the back with a blue background.  On the card:
Dorn Pevsky, Operations Manager, dorn@brovalux-example.com
47215-K Harlow Ave. 9 #382
Pinecrest, IN 47912
555.604.2817, 888.555.4163

Updates
please include cell 555.318.6247
                                   
Thank you
If possible the fading logo on the front should be very subtle and light and lets look at centering that as well
thanks

```html
<!DOCTYPE html>
<html lang="en">
<head>
<meta charset="utf-8">
<title>Brovalux Business Card</title>
<link rel="stylesheet" href="https://fonts.googleapis.com/css2?family=Open+Sans:wght@400;600;700&display=swap">
<style>
  :root {
    --backdrop: #c9c9c9;
    --brand-blue: #0e75bf;
    --band-dark: #3b3b3d;
    --paper: #ffffff;
    --ink-light: #ffffff;
    --rule: rgba(255, 255, 255, 0.55);
  }
  * { box-sizing: border-box; margin: 0; padding: 0; }
  html, body {
    width: 1200px;
    height: 960px;
    overflow: hidden;
  }
  body {
    position: relative;
    background: var(--backdrop);
    font-family: "Open Sans", Arial, sans-serif;
  }
  .card {
    position: absolute;
    overflow: hidden;
  }

  /* Back of card: blue field with white wordmark */
  .card-back {
    left: 305px;
    top: 58px;
    width: 649px;
    height: 388px;
    background: var(--brand-blue);
  }
  .card-back .brand {
    position: absolute;
    left: 114px;
    top: 129px;
    display: flex;
    align-items: center;
    gap: 22px;
  }
  .card-back .brand-mark {
    width: 106px;
    height: 106px;
    border-radius: 50%;
    background: var(--ink-light);
  }
  .card-back .brand-name {
    font-size: 58px;
    font-weight: 700;
    color: var(--ink-light);
    letter-spacing: 0.5px;
  }
  .card-back .web-band {
    position: absolute;
    left: 0;
    bottom: 0;
    width: 100%;
    height: 32px;
    background: var(--band-dark);
    color: var(--ink-light);
    font-size: 20px;
    line-height: 32px;
    text-align: center;
    padding-left: 60px;
  }

  /* Front of card: white logo panel over blue contact panel */
  .card-front {
    left: 292px;
    top: 496px;
    width: 664px;
    height: 398px;
    background: var(--brand-blue);
  }
  .card-front .logo-panel {
    position: absolute;
    left: 0;
    top: 0;
    width: 100%;
    height: 186px;
    background: var(--paper);
  }
  .card-front .brand {
    position: absolute;
    left: 151px;
    top: 52px;
    display: flex;
    align-items: center;
    gap: 20px;
  }
  .card-front .brand-mark {
    width: 92px;
    height: 92px;
    border-radius: 50%;
    background: var(--brand-blue);
  }
  .card-front .brand-name {
    font-size: 48px;
    font-weight: 700;
    color: var(--brand-blue);
    letter-spacing: 0.5px;
  }
  .card-front .person {
    position: absolute;
    left: 55px;
    top: 257px;
    color: var(--ink-light);
  }
  .person .person-name {
    font-size: 29px;
    font-weight: 600;
    line-height: 1.1;
  }
  .person .person-title {
    font-size: 13px;
    font-weight: 600;
    margin-top: 2px;
  }
  .card-front .divider {
    position: absolute;
    left: 357px;
    top: 214px;
    width: 1px;
    height: 156px;
    background: var(--rule);
  }
  .card-front .contact {
    position: absolute;
    left: 392px;
    top: 204px;
    color: var(--ink-light);
    font-style: normal;
    font-size: 15px;
    line-height: 21px;
    white-space: nowrap;
  }
  .contact .company {
    font-size: 16px;
    font-weight: 700;
    line-height: 22px;
    margin-bottom: 3px;
  }
</style>
</head>
<body>

  <section class="card card-back" aria-label="Business card back">
    <div class="brand">
      <span class="brand-mark" aria-hidden="true"></span>
      <span class="brand-name">brovalux</span>
    </div>
    <div class="web-band">www.brovalux-example.com</div>
  </section>

  <section class="card card-front" aria-label="Business card front">
    <div class="logo-panel">
      <div class="brand">
        <span class="brand-mark" aria-hidden="true"></span>
        <span class="brand-name">brovalux</span>
      </div>
    </div>

    <div class="person">
      <p class="person-name">Dorn Pevsky</p>
      <p class="person-title">Operations Manager</p>
    </div>

    <div class="divider" aria-hidden="true"></div>

    <address class="contact">
      <p class="company">Brovalux Building Services</p>
      <p>47215-K Harlow Ave. 9 #382</p>
      <p>Pinecrest, IN 47912</p>
      <p>Phone&nbsp; 888.555.4163</p>
      <p>Cell&nbsp; 555.318.6247</p>
      <p>Fax&nbsp; 555.604.2817</p>
      <p>E-mail&nbsp; dorn@brovalux-example.com</p>
      <p>www.brovalux-example.com</p>
    </address>
  </section>

</body>
</html>
```